Gutschein für Onlineshop DIN A Lang
Zielgruppe
Wir betreiben unter www.feldkiste-online.example einen Onlineshop für Armee- und Outdoorbekleidung sowie Ausrüstung. Für eine Paketbeilage benötigen wir einen Gutschein
Aufgabenstellung
Erstellung eines Gutscheins im DIN A Lang Format (Kuvert) mit Vorder- und Rückseite im CI der Webseite. Logo kann gerne zur Verfügung gestellt werden.
Gutscheincode, Wert und Laufzeit wird noch mitgeteilt.

```html
<!DOCTYPE html>
<html lang="de">
<head>
<meta charset="utf-8">
<title>Feldkiste Gutschein – Vorder- und Rückseite</title>
<link href="https://fonts.googleapis.com/css2?family=Arimo:wght@400;700&family=Stardos+Stencil:wght@700&display=swap" rel="stylesheet">
<style>
  :root {
    --bg: #e9e6e0;
    --paper: #ffffff;
    --olive-dark: #4b5339;
    --olive: #8f9b6a;
    --olive-light: #c6cf9e;
    --ink: #2b2b2b;
    --camo-sand: #c9ab78;
    --camo-green: #5f6845;
    --url-orange: #8a4a12;
  }
  * { box-sizing: border-box; margin: 0; padding: 0; }
  html, body { width: 1200px; height: 1200px; overflow: hidden; }
  body { background: var(--bg); font-family: "Arimo", Arial, sans-serif; color: var(--ink); position: relative; }

  .voucher {
    position: absolute; left: 100px; width: 1000px; height: 476px;
    background: var(--paper); padding: 12px;
    box-shadow: 0 4px 14px rgba(0,0,0,.18);
  }
  .voucher--front { top: 94px; }
  .voucher--back { top: 630px; }
  .voucher__inner { position: relative; width: 100%; height: 100%; overflow: hidden; }

  .brand { display: flex; align-items: center; gap: 8px; font-family: "Arimo", Arial, sans-serif; font-weight: 700; color: var(--olive-dark); font-size: 30px; }
  .brand__square { width: 16px; height: 16px; background: var(--olive); }

  /* Front */
  .front__camo { position: absolute; left: 0; top: 0; width: 84px; height: 100%;
    background: linear-gradient(180deg, var(--camo-green), var(--camo-sand) 55%, var(--camo-green)); }
  .front__info { position: absolute; left: 84px; top: 0; width: 206px; height: 100%; background: var(--paper); padding: 34px 10px 0 14px; }
  .front__info p { font-size: 14.5px; line-height: 1.3; margin-bottom: 18px; }
  .front__info .front__text { position: absolute; left: 14px; right: 6px; top: 270px; }
  .front__url { position: absolute; left: 14px; bottom: 14px; font-weight: 700; font-size: 15.5px; }
  .front__photo { position: absolute; left: 290px; top: 0; right: 0; height: 100%;
    background: linear-gradient(160deg, var(--camo-green) 0%, #2f3030 25%, var(--camo-sand) 55%, #b79a66 80%, var(--camo-green) 100%); }
  .band { position: absolute; background: var(--olive); color: #fff; font-family: "Stardos Stencil", "Courier New", monospace; font-weight: 700; line-height: 1; }
  .band--title { left: 470px; top: 132px; right: -10px; height: 104px; font-size: 84px; padding: 10px 0 0 24px; }
  .band--value { left: 760px; top: 250px; right: -10px; height: 104px; font-size: 86px; padding: 10px 0 0 40px; }

  /* Back */
  .back__panel { position: absolute; left: 0; top: 0; width: 330px; height: 100%; background: var(--olive-dark); color: #fff; padding: 58px 26px 0 32px; }
  .back__value { font-family: "Stardos Stencil", "Courier New", monospace; font-weight: 700; font-size: 104px; line-height: 1; letter-spacing: 2px; }
  .back__title { font-family: "Stardos Stencil", "Courier New", monospace; font-weight: 700; font-size: 50px; line-height: 1; margin-top: 8px; }
  .back__label { font-size: 13px; margin-top: 44px; }
  .back__code { margin-top: 8px; background: var(--olive-light); color: var(--olive-dark); font-size: 30px; letter-spacing: 1px; height: 42px; line-height: 42px; padding-left: 22px; }
  .back__terms { margin-top: 12px; font-size: 12.5px; line-height: 1.35; text-align: justify; }
  .back__photo { position: absolute; left: 330px; top: 0; right: 0; height: 100%;
    background: linear-gradient(180deg, #3e5c80 0%, #7f93a8 35%, #c9c2b0 55%, #e8a04a 78%, #d9661c 92%, #3a2a22 100%); }
  .back__logo { position: absolute; right: 42px; top: 0; width: 176px; height: 118px; background: var(--paper); display: flex; align-items: center; justify-content: center; }
  .back__benefits { position: absolute; left: 630px; top: 194px; width: 330px; list-style: none; }
  .back__benefits li { position: relative; padding-left: 18px; font-size: 14.5px; font-weight: 700; color: #2f2f2f; line-height: 1.3; margin-bottom: 10px; }
  .back__benefits svg { position: absolute; left: 0; top: 4px; width: 12px; height: 11px; }
  .back__url { position: absolute; right: 26px; bottom: 22px; font-weight: 700; font-size: 15.5px; color: var(--url-orange); }
</style>
</head>
<body>

<section class="voucher voucher--front">
  <div class="voucher__inner">
    <div class="front__camo" role="img" aria-label="Tarnmuster-Stoff"></div>
    <div class="front__info">
      <div class="brand"><span class="brand__square"></span>Feldkiste</div>
      <div class="front__text">
        <p>Einer der ältesten Online-Armee Versender.</p>
        <p>Große Auswahl an Bekleidung &amp; Ausrüstung für Hobby, Freizeit und Beruf.</p>
      </div>
      <div class="front__url">www.feldkiste-online.example</div>
    </div>
    <div class="front__photo" role="img" aria-label="Messer mit Scheide, Erkennungsmarken und Rucksack auf Tarnstoff"></div>
    <div class="band band--title">GUTSCHEIN</div>
    <div class="band band--value">25€</div>
  </div>
</section>

<section class="voucher voucher--back">
  <div class="voucher__inner">
    <div class="back__panel">
      <div class="back__value">25 €</div>
      <div class="back__title">GUTSCHEIN</div>
      <div class="back__label">Ihr Gutscheincode:</div>
      <div class="back__code">1234567890</div>
      <p class="back__terms">Einmalig einlösbar bis zum XX.XX.2014 unter <strong>www.muster.example</strong>. Nicht mit anderen Aktionen kombiniertbar. Nur ein Gutschein pro Kunde.</p>
    </div>
    <div class="back__photo" role="img" aria-label="Zwei Wanderer mit Rucksäcken auf einem Felsen bei Sonnenuntergang"></div>
    <div class="back__logo"><div class="brand"><span class="brand__square"></span>Feldkiste</div></div>
    <ul class="back__benefits">
      <li><svg viewBox="0 0 12 11"><path d="M1 6l3.5 3.5L11 1.5" fill="none" stroke="#2f2f2f" stroke-width="2.2"/></svg>fast 10 Jahre Bundeswehr-Shop im Internet</li>
      <li><svg viewBox="0 0 12 11"><path d="M1 6l3.5 3.5L11 1.5" fill="none" stroke="#2f2f2f" stroke-width="2.2"/></svg>größen Auswahl an Bundeswehrbekleidung, Armeebekleidung sowie umfangreiche Ausrüstung für Arbeit, Hobby und Freizeit</li>
      <li><svg viewBox="0 0 12 11"><path d="M1 6l3.5 3.5L11 1.5" fill="none" stroke="#2f2f2f" stroke-width="2.2"/></svg>sofort Lieferung in 24 Stunden</li>
    </ul>
    <div class="back__url">www.feldkiste-online.example</div>
  </div>
</section>

</body>
</html>
```